Wordpress Design for a Business Blog

We are running the finance blog lumo.net and want to renew our web page design. Thus, we need a new designed Wordpress theme containing an overview page, used on the front page and the start pages of the categories, and a single article view like on http://lumo.net/blog/coping-with-falling-dollar/ . The new look should be serious, should contain all elements of the current website, should look professional (no entertainment elements) and in light colors.
Updates

Reason: Due to some request, we've extended the deadline a few days.

Reason: Hello,

we received a comment that our budget is to low for  a complete Wordpress design including coding. Thus, we changed our requriement to psd design  only,  without coding.

Industry/Entity Type

Entertainment

Requirements
Must have
• * Light colors
* Two column layout
* Contain all elements of the current website www.lumo.net
Should not have
• * Too much colors
* Look to flashy

```html
<!DOCTYPE html>
<html lang="en">
<head>
<meta charset="utf-8">
<title>lumo.net – Finance Blog</title>
<link href="https://fonts.googleapis.com/css2?family=Arimo:wght@400;700&family=Oswald:wght@500;600&family=Gelasio:wght@400&display=swap" rel="stylesheet">
<style>
:root{
  --green-dark:#5b9a06;
  --green:#7fbf12;
  --green-light:#a9dc3a;
  --blue:#1f6fa8;
  --blue-dark:#15507d;
  --blue-box:#2278b2;
  --link:#1a6fb5;
  --text:#333;
  --panel:#eef0f0;
  --panel-border:#c9cccc;
  --page:#f4f5f5;
  --footer:#0d3d6b;
  --orange:#f07a16;
  --white:#fff;
}
*{box-sizing:border-box;margin:0;padding:0}
html,body{width:759px;height:1200px;overflow:hidden}
body{background:var(--page);font-family:Arimo,Arial,sans-serif;color:var(--text);position:relative}
a{color:var(--link);text-decoration:none}

.site-header{position:absolute;left:0;top:0;width:759px;height:119px;
  background:linear-gradient(180deg,#6fae0b 0%,#8cc51d 45%,#9fd431 100%);overflow:hidden}
.site-header .sheen{position:absolute;right:0;top:0;width:420px;height:119px;
  background:linear-gradient(200deg,rgba(255,255,255,.18),rgba(255,255,255,0) 60%)}
.top-bar{position:absolute;right:0;top:0;height:30px;width:390px;background:linear-gradient(#2a86c6,#1a64a0);
  border-radius:0 0 0 16px;display:flex;align-items:center;padding-left:22px;gap:16px}
.top-bar a{color:var(--white);font-size:11px}
.search{margin-left:6px;width:177px;height:19px;background:var(--white);border-radius:10px;display:flex;align-items:center;
  padding:0 8px;font-size:8px;color:#999;justify-content:space-between}
.brand{position:absolute;left:16px;top:48px;font-family:Arimo,Arial,sans-serif;font-weight:700;font-size:34px;color:var(--white);letter-spacing:-1px}
.tagline{position:absolute;left:221px;top:55px;font-family:Oswald,Arial,sans-serif;font-weight:500;font-size:21px;color:var(--white);letter-spacing:.2px}

.main-nav{position:absolute;left:0;top:119px;width:759px;height:41px;background:linear-gradient(#8ccd24,#5d9f07);
  border-top:1px solid #b6e35a}
.main-nav a{position:absolute;top:7px;color:#111;font-size:12.5px;height:26px;line-height:26px;white-space:nowrap}
.main-nav a.current{background:linear-gradient(#fff,#e2e2e2);border-radius:3px;padding:0 11px}
.rss{position:absolute;left:713px;top:6px;width:30px;height:29px}

.content{position:absolute;left:9px;top:168px;width:543px;height:968px;background:var(--panel);border:1px solid var(--panel-border);padding:0 7px}
.post{height:184px;position:relative}
.post h2{font-weight:400;font-size:14.5px;color:var(--link);padding-top:10px;height:30px}
.meta{font-size:8.6px;border-bottom:1px dotted #555;padding-bottom:3px;color:#111}
.meta b{font-weight:700}
.post-body{display:flex;justify-content:space-between;margin-top:8px}
.excerpt{width:340px;font-size:8.6px;line-height:13px}
.excerpt p+p{margin-top:13px}
.thumb-wrap{width:172px}
.thumb{width:172px;height:111px;border:1px solid #ccc;box-shadow:0 1px 2px rgba(0,0,0,.2)}
.t-cartoon{background:linear-gradient(#fafafa,#ddd)}
.t-weight{background:radial-gradient(circle at 45% 55%,#b9b9b9,#f2f2f2 60%)}
.t-note{background:linear-gradient(135deg,#e8e8e8,#555 50%,#e6e6e6)}
.t-key{background:radial-gradient(circle at 50% 40%,#ffffff,#d9d9d9 70%)}
.share{display:flex;gap:5px;margin:7px 0 0 8px}
.share span{width:17px;height:17px;border-radius:3px}
.read-more{position:absolute;left:436px;top:1108px;background:linear-gradient(#5fae28,#2e7d0e);color:var(--white);font-family:Oswald,Arial,sans-serif;font-weight:500;font-size:13px;width:110px;height:30px;line-height:30px;text-align:center;border-radius:2px}
.rule{position:absolute;left:16px;width:529px;top:1092px;border-top:1px dashed #666}

.sidebar{position:absolute;left:560px;top:170px;width:186px}
.box{border-radius:8px;position:absolute;left:0;width:186px;color:var(--white);overflow:hidden}
.ad{background:linear-gradient(#f1f2f2,#dadcdc);border:1px solid #888;color:#000;font-family:Gelasio,Georgia,serif;font-size:17px;display:flex;align-items:center;justify-content:center}
.box.blue{background:linear-gradient(#2f8bc8,#1d6aa4);border:1px solid #1a5f92}
.box.green{background:linear-gradient(#6fb31d,#4f9310);border:1px solid #468310}
.box h3{font-family:Gelasio,Georgia,serif;font-weight:400;font-size:18px;padding:5px 9px 4px}
.box ul{list-style:none;padding:2px 12px 0 14px}
.box li{font-size:8.3px;line-height:11px;margin-bottom:7px;padding-left:10px;position:relative}
.box li::before{content:"";position:absolute;left:0;top:4px;width:3px;height:3px;background:var(--white)}
.box.popular li{line-height:10px;margin-bottom:4px}
.archive-select{margin:2px 8px;height:15px;background:var(--white);color:#333;font-size:8px;padding:2px 4px;display:flex;justify-content:space-between;align-items:center}
.archive-select i{width:13px;height:11px;background:#111;display:block}
.tags{padding:0 10px;line-height:17px;font-size:10px}
.tags .s{font-size:11.5px}
.tags .m{font-size:13px}
.tags .l{font-size:14px}

.site-footer{position:absolute;left:0;top:1144px;width:759px;height:56px;background:var(--footer);color:var(--white);text-align:center;font-size:8.3px;padding-top:24px;line-height:12px}
</style>
</head>
<body>
<header class="site-header">
  <div class="sheen"></div>
  <nav class="top-bar"><a href="#">About</a><a href="#">Tag Cloud</a>
    <div class="search"><span>Type your search here</span>
      <svg width="12" height="12" viewBox="0 0 12 12"><circle cx="7" cy="5" r="3.5" fill="none" stroke="#222" stroke-width="1.5"/><line x1="4.5" y1="7.5" x2="1.5" y2="10.5" stroke="#222" stroke-width="2"/></svg></div>
  </nav>
  <div class="brand">Lumo.net</div>
  <div class="tagline">LUMO.NET IS ALL ABOUT ACHIEVING YOUR FINANCIAL GOALS</div>
</header>

<nav class="main-nav">
  <a class="current" href="#" style="left:9px">Home</a>
  <a href="#" style="left:77px">Finance</a>
  <a href="#" style="left:144px">Economy</a>
  <a href="#" style="left:219px">Resources</a>
  <a href="#" style="left:300px">Personal Saving</a>
  <a href="#" style="left:410px">Make Money</a>
  <a href="#" style="left:504px">Miscellanious</a>
  <a href="#" style="left:600px">Uncategorized</a>
  <svg class="rss" viewBox="0 0 30 29" role="img" aria-label="Feed"><rect width="30" height="29" rx="5" fill="#f07a16"/><circle cx="9" cy="21" r="2.5" fill="#fff"/><path d="M7 13a9 9 0 0 1 9 9M7 7a15 15 0 0 1 15 15" stroke="#fff" stroke-width="3" fill="none"/></svg>
</nav>

<main class="content">
  <article class="post">
    <h2>Money/ Saving Jokes</h2>
    <div class="meta"><b>Posted by Dana</b> in <a href="#">Economy,Finance,Miscellaneous,Personal Saving,Resources,Uncategorized</a> <b>on June 1, 2011 &nbsp; | no responses</b></div>
    <div class="post-body">
      <div class="excerpt"><p>Here are some jokes about money/ saving I found online. I hope you'll have fun reading them. Enjoy! My mother decided to trim her household budget wherever possible, so instead of having a dress dry-cleaned she washed it by hand. Proud of her savings, she boasted to my father, "Just think, Fred, we are five […]</p><p>Here are some jokes about money/ saving I found online. I hope you'll have fun reading them. Enjoy! My mother decided to trim her household budget wherever possible, so instead of having a dress dry-cleaned she washed it by hand. Proud of her savings, she boasted to my father, "Just think, Fred, we are five […]</p></div>
      <div class="thumb-wrap"><div class="thumb t-cartoon" role="img" aria-label="Cartoon of a couple talking about household savings"></div>
        <div class="share"><span style="background:#3b5998"></span><span style="background:#7cc22c"></span><span style="background:#9fb6d8"></span><span style="background:#356aa0"></span><span style="background:#3a9a3a"></span><span style="background:#1d2f8f"></span><span style="background:#5fb42a"></span></div></div>
    </div>
  </article>
  <article class="post">
    <h2>Money/ Saving Jokes</h2>
    <div class="meta"><b>Posted by Dana</b> in <a href="#">Economy,Finance,Miscellaneous,Personal Saving,Resources,Uncategorized</a> <b>on June 1, 2011 &nbsp; | no responses</b></div>
    <div class="post-body">
      <div class="excerpt"><p>Here are some jokes about money/ saving I found online. I hope you'll have fun reading them. Enjoy! My mother decided to trim her household budget wherever possible, so instead of having a dress dry-cleaned she washed it by hand. Proud of her savings, she boasted to my father, "Just think, Fred, we are five […]</p><p>Here are some jokes about money/ saving I found online. I hope you'll have fun reading them. Enjoy! My mother decided to trim her household budget wherever possible, so instead of having a dress dry-cleaned she washed it by hand. Proud of her savings, she boasted to my father, "Just think, Fred, we are five […]</p></div>
      <div class="thumb-wrap"><div class="thumb t-weight" role="img" aria-label="Euro sign chained to a ball and chain"></div>
        <div class="share"><span style="background:#3b5998"></span><span style="background:#7cc22c"></span><span style="background:#9fb6d8"></span><span style="background:#356aa0"></span><span style="background:#3a9a3a"></span><span style="background:#1d2f8f"></span><span style="background:#5fb42a"></span></div></div>
    </div>
  </article>
  <article class="post">
    <h2>Surviving the Euro Crisis</h2>
    <div class="meta"><b>Posted by Theo</b> in <a href="#">Economy,Finance,Miscellaneous,Personal Saving,Resources,Uncategorized</a> <b>on May 20, 2011 &nbsp; | no responses</b></div>
    <div class="post-body">
      <div class="excerpt"><p>Aside from the falling dollar, the global economy today is also struggling with the Euro crisis. To prevent a second financial crisis, definite and strict measures must be taken to stabilize not only Europe but the worldwide economy as a whole. Germany is trying to solve this dilemma by regulating the markets and pacifying the .</p><p>Aside from the falling dollar, the global economy today is also struggling with the Euro crisis. To prevent a second financial crisis, definite and strict measures must be taken to stabilize not only Europe but the worldwide economy as a whole. Germany is trying to solve this dilemma by regulating the markets and pacifying the</p></div>
      <div class="thumb-wrap"><div class="thumb t-note" role="img" aria-label="Crumpled banknote"></div>
        <div class="share"><span style="background:#3b5998"></span><span style="background:#7cc22c"></span><span style="background:#9fb6d8"></span><span style="background:#356aa0"></span><span style="background:#3a9a3a"></span><span style="background:#1d2f8f"></span><span style="background:#5fb42a"></span></div></div>
    </div>
  </article>
  <article class="post">
    <h2>6 Secrets to Successful Saving</h2>
    <div class="meta"><b>Posted by Dana</b> in <a href="#">Economy,Finance,Miscellaneous,Personal Saving,Resources,Uncategorized</a> <b>on April 29, 2011 &nbsp; | no responses</b></div>
    <div class="post-body">
      <div class="excerpt"><p>Like they say, you are never too young nor too old to start saving. Especially in today's hard times, we should always be ready for emergencies and other unexpected expenses. So here are six secrets that might just help you to finally succeed in your savings plan. Secret #1: A Realistic, Achievable Savings Goal. Realistic, […]</p><p>Like they say, you are never too young nor too old to start saving. Especially in today's hard times, we should always be ready for emergencies and other unexpected expenses. So here are six secrets that might just help you to finally succeed in your savings plan. Secret #1: A Realistic, Achievable Savings Goal. Realistic, […]</p></div>
      <div class="thumb-wrap"><div class="thumb t-key" role="img" aria-label="Keyboard key labelled Save beside a few coins"></div>
        <div class="share"><span style="background:#3b5998"></span><span style="background:#7cc22c"></span><span style="background:#9fb6d8"></span><span style="background:#356aa0"></span><span style="background:#3a9a3a"></span><span style="background:#1d2f8f"></span><span style="background:#5fb42a"></span></div></div>
    </div>
  </article>
  <article class="post">
    <h2>6 Secrets to Successful Saving</h2>
    <div class="meta"><b>Posted by Dana</b> in <a href="#">Economy,Finance,Miscellaneous,Personal Saving,Resources,Uncategorized</a> <b>on April 29, 2011 &nbsp; | no responses</b></div>
    <div class="post-body">
      <div class="excerpt"><p>Like they say, you are never too young nor too old to start saving. Especially in today's hard times, we should always be ready for emergencies and other unexpected expenses. So here are six secrets that might just help you to finally succeed in your savings plan. Secret #1: A Realistic, Achievable Savings Goal. Realistic, […]</p><p>Like they say, you are never too young nor too old to start saving. Especially in today's hard times, we should always be ready for emergencies and other unexpected expenses. So here are six secrets that might just help you to finally succeed in your savings plan. Secret #1: A Realistic, Achievable Savings Goal. Realistic, […]</p></div>
      <div class="thumb-wrap"><div class="thumb t-key" role="img" aria-label="Keyboard key labelled Save beside a few coins"></div>
        <div class="share"><span style="background:#3b5998"></span><span style="background:#7cc22c"></span><span style="background:#9fb6d8"></span><span style="background:#356aa0"></span><span style="background:#3a9a3a"></span><span style="background:#1d2f8f"></span><span style="background:#5fb42a"></span></div></div>
    </div>
  </article>
</main>
<div class="rule"></div>
<a class="read-more" href="#">Read More Posts</a>

<aside class="sidebar">
  <div class="box ad" style="top:0;height:127px">Advertisement</div>
  <div class="box ad" style="top:136px;height:125px">Advertisement</div>
  <section class="box blue" style="top:271px;height:60px"><h3>Archives</h3>
    <div class="archive-select"><span>Select Month</span><i></i></div></section>
  <section class="box blue popular" style="top:339px;height:129px"><h3>Popular Posts</h3>
    <ul><li>Will You Inherit Your Parents' Debt?</li><li>Money Saving Quotes</li><li>Product Labels: More Than Meets The Eye</li><li>Money Saving Quotes</li><li>Product Labels: More Than Meets The</li></ul></section>
  <section class="box blue" style="top:476px;height:166px"><h3>Categories</h3>
    <ul><li>Finance (38)</li><li>Economy (31)</li><li>Resources (44)</li><li>Personal Saving (45)</li><li>Make Money (13)</li><li>Miscellaneous (53)</li><li>Uncategorized (11)</li></ul></section>
  <section class="box green" style="top:648px;height:166px"><h3>Tags</h3>
    <p class="tags">financial planner <span class="s">financial planning</span> financial planning process <span class="m">frugal lifestyle</span> frugal living <span class="l">overspending</span> personal savings retirement <span class="m">save money</span> <span class="m">unemployment</span> More Tags</p></section>
  <section class="box blue" style="top:822px;height:67px"><h3>Blogroll</h3>
    <ul><li>Seekwise.com</li></ul></section>
</aside>

<footer class="site-footer">
  Terms &amp; Conditions | FAQs | Contact Us | About Us<br>
  ©2011 Copyright &nbsp;lumo.net &nbsp; | &nbsp;All Rights Reserved
</footer>
</body>
</html>
```